Building Custom Homes

We need a new business card design for a new company called " T & R Custom Homes" . We built custom homes according to our client's dream home. We would like to see designs that use the color blue, green, yellow, orange, pink depicting a home happy 'n bright!

Industry/Entity Type

Business

Contact Information for Business Card

Email: porvinta73@kelbrix.com.au Mobile: 0427 318 946 Phone: 02 6781 4053 Address: Shop 3 / 72 Wexbury Street Coffs Harbour, NSW 2450 Builders License Number : 47 08 3K ABN : 63 519 874 027 Name: Owen Bask

Colors
0355a3
0392cd
9bcb3c
e34297
f78f20
fbed22

Requirements
Must have
• The Company Name : "T & R Custom Homes"
• must depict the building industry

```html
<!DOCTYPE html>
<html lang="en">
<head>
<meta charset="utf-8">
<title>T &amp; R Custom Homes — Business Card</title>
<link href="https://fonts.googleapis.com/css2?family=Mulish:wght@400;700&display=swap" rel="stylesheet">
<style>
  :root {
    --page-bg: #ececec;
    --card-bg: #ffffff;
    --card-edge: #bdbdbd;
    --ink: #3a3a3a;
    --ink-soft: #4a4a4a;
    --brand-navy: #0355a3;
    --brand-blue: #0392cd;
    --brand-green: #9bcb3c;
    --brand-pink: #e34297;
    --brand-orange: #f78f20;
    --brand-yellow: #fbed22;
  }
  html, body {
    margin: 0;
    padding: 0;
    width: 1164px;
    height: 1200px;
    overflow: hidden;
    background: var(--page-bg);
    font-family: "Mulish", Arial, sans-serif;
  }
  .business-card {
    position: absolute;
    left: 82px;
    top: 264px;
    width: 1000px;
    height: 672px;
    background: var(--card-bg);
    border: 2px solid var(--card-edge);
    box-sizing: border-box;
    color: var(--ink);
  }
  .company-name {
    position: absolute;
    left: 55px;
    top: 72px;
    margin: 0;
    font-size: 40px;
    font-weight: 700;
    letter-spacing: 0.2px;
  }
  .person-name {
    position: absolute;
    right: 93px;
    top: 262px;
    margin: 0;
    font-size: 56px;
    font-weight: 700;
  }
  .accent-bar {
    position: absolute;
    right: -2px;
    top: 241px;
    width: 40px;
    height: 104px;
    display: flex;
    flex-direction: column;
  }
  .accent-bar span { flex: 1; }
  .accent-bar .blue   { background: var(--brand-blue); }
  .accent-bar .green  { background: var(--brand-green); }
  .accent-bar .yellow { background: var(--brand-yellow); }
  .accent-bar .orange { background: var(--brand-orange); }
  .accent-bar .pink   { background: var(--brand-pink); }
  .address-block {
    position: absolute;
    left: 18px;
    top: 506px;
    display: flex;
    gap: 16px;
    font-size: 21px;
    line-height: 32px;
    color: var(--ink-soft);
  }
  .address-block p { margin: 0; }
  .contact-block {
    position: absolute;
    left: 600px;
    top: 498px;
    font-size: 22px;
    line-height: 32px;
    color: var(--ink-soft);
  }
  .contact-row {
    display: flex;
    align-items: center;
    gap: 14px;
  }
  .contact-row.indent { padding-left: 32px; }
  .contact-row.email { margin-top: 6px; }
  .icon { width: 18px; height: 18px; flex: none; }
  .icon-home  { fill: var(--brand-navy); margin-top: 7px; }
  .icon-phone { fill: var(--brand-green); }
  .icon-mail  { fill: none; stroke: var(--brand-orange); stroke-width: 1.8; }
</style>
</head>
<body>
  <section class="business-card">
    <h1 class="company-name">T &amp; R Custom Homes</h1>
    <h2 class="person-name">Owen Bask</h2>
    <div class="accent-bar" aria-hidden="true">
      <span class="blue"></span>
      <span class="green"></span>
      <span class="yellow"></span>
      <span class="orange"></span>
      <span class="pink"></span>
    </div>

    <div class="address-block">
      <svg class="icon icon-home" viewBox="0 0 20 20" aria-hidden="true">
        <path d="M10 2 L19 10 H16 V18 H12 V13 H8 V18 H4 V10 H1 Z"/>
      </svg>
      <p>Address: Shop 3 / 72 Wexbury Street Coffs<br>
        Harbour, NSW 2450 Builders License<br>
        Number : 47 08 3K ABN : 63 519 874 027</p>
    </div>

    <div class="contact-block">
      <div class="contact-row">
        <svg class="icon icon-phone" viewBox="0 0 20 20" aria-hidden="true">
          <path d="M5 2 L8 6 L6.5 8 C7.5 10.5 9.5 12.5 12 13.5 L14 12 L18 15 L16 18 C9 18 2 11 2 4 Z"/>
        </svg>
        <span>0427 318 946</span>
      </div>
      <div class="contact-row indent"><span>02 6781 4053</span></div>
      <div class="contact-row email">
        <svg class="icon icon-mail" viewBox="0 0 20 20" aria-hidden="true">
          <path d="M2 5 H18 V15 H2 Z M3 6 L10 11 L17 6"/>
        </svg>
        <span>porvinta73@kelbrix.com.au</span>
      </div>
    </div>
  </section>
</body>
</html>
```